Need a Web Site Design - Fresh, Modern, and Visually Engaging Website Design

I’m looking to create a clean, modern, and visually appealing website that effectively represents our brand and services. The design should focus on user experience, intuitive navigation, and a professional aesthetic.

The Home page should set the tone for the entire site, featuring a sleek, modern layout with strong visual appeal.

Our Company Logo colors attached. The design can incorporate this color theme or use a unique palette that complements it.

Site Map:
We will begin with the following sections, with the potential to expand and add more services in the future:

Home: A welcoming and engaging introduction to our business, highlighting key services and industries we serve.
About Us: Share our story, mission, and values to connect with visitors.
Software Development: Showcase our expertise in developing innovative software solutions.
Industries We Serve: Provide detailed insights into the sectors we specialize in, including:
- Payroll Sector
- Education
- Transportation
- Home Care Services
Contact Us: Offer easy ways for clients to reach out, including forms and contact details.
Footer: Include essential links, social media handles, and company details.

Draft content for Services Page
Services
We specialize in delivering tailored solutions to meet your business needs. Our expertise spans Product Development, App Development, and Website Development.

1. Product Development
From concept to completion, we help you bring innovative products to life.
What We Offer:
• Custom Software Solutions: Scalable and secure software tailored to your business processes.
• Prototyping & MVP Development: Rapid prototyping and Minimum Viable Product creation to validate ideas.
• End-to-End Development: Comprehensive support from ideation to launch.
• Integration Services: Seamless integration of new products with your existing systems.

2. App Development
Build cutting-edge mobile and desktop applications to engage your audience and enhance operational efficiency.
What We Offer:
• Native & Cross-Platform Apps: Applications built for iOS, Android, and cross-platform frameworks.
• User-Centered Design: Apps designed with intuitive interfaces and smooth user experiences.
• Custom Features: Tailored functionality to meet your unique business needs.
• Maintenance & Updates: Continuous support to keep your app relevant and high-performing.

3. Website Development
Your website is the face of your business. We ensure it leaves a lasting impression.
What We Offer:
• Custom Website Design: Unique and responsive designs tailored to your brand identity.
• E-Commerce Development: Scalable and secure online stores to grow your business.
• CMS Integration: Easy-to-manage content systems like WordPress, Joomla, or custom CMS.
• SEO Optimization: Built-in search engine optimization for enhanced visibility.

Your Journey with Us
Our streamlined approach ensures that your project is handled with precision, creativity, and care. We partner with you at every step to create tailored solutions that transform your business.

Phase One: Discovery
We start by understanding your business inside and out, ensuring the foundation for our partnership is built on knowledge and alignment.
Assessment & Analysis
We dive deep into your business environment to uncover challenges, identify growth opportunities, and understand the economic factors driving your operations.
Process Evaluation
Our team analyzes your current workflows and processes, identifying inefficiencies and areas where improvements can enhance productivity and effectiveness.
Data-Driven Strategy
Using your organization’s technical and operational data, we create informed strategies that align with your goals and drive meaningful outcomes.

Phase Two: Estimate
We present a fully customized solution tailored to your needs, empowering you with the information required to make confident decisions.
Technology Plan & Roadmap
We design a detailed technology roadmap that includes the functionalities you need, the ideal tools and technologies, and a timeline for project completion.
Transition Planning
Our scope includes planning for a seamless transition, covering everything from system migration to user training and long-term usability.
Future Forecasting
Our solutions are built to grow with your business. We consider scalability, future technology trends, and your organization’s long-term needs to ensure lasting success.

Phase Three: Blueprint
Every successful project begins with a comprehensive plan. Our blueprints define every aspect of functionality, technology, and user experience, ensuring a smooth path forward.
Technology and Architecture
We develop a detailed framework outlining the infrastructure, external integrations, security measures, and scalability plans for the project.
Interactive Prototype
We create a clickable prototype that showcases the design, user interface, and functionality of the system, ensuring alignment with your vision.
Engineering & Testing Plan
Our strategy includes step-by-step engineering and rigorous testing for quality, security, and scalability throughout the development process.
Risk Management
We anticipate potential risks and outline mitigation strategies, reducing surprises and keeping the project on track.

Phase Four: Engineering
Our team of expert software engineers transforms the blueprint into a robust, scalable system tailored to your needs.
Full-Service Teams
We assemble a specialized team for your project, ensuring the skills and expertise align with your business goals and technical requirements.
Strategic Delivery
Our phased development approach delivers essential features first, reducing risks and enabling faster time-to-market.
Close Collaboration with Clients
We keep you informed and involved through every sprint, ensuring your vision is realized from the MVP to the final release.

Phase Five: Training & Support
We ensure a smooth integration of your new software, provide training for your team, and offer ongoing support to guarantee success.
Smooth Transition
We work with you to test new modules, retire outdated systems, and ensure a seamless rollout of the new solution.
Teamwide Training
Our team provides comprehensive training, gathers performance feedback, and optimizes the system for peak efficiency.
Long-Term Support
We continue to refine and improve the system post-launch, introducing enhancements to keep you ahead of the curve.

Our Projects
Explore our portfolio of completed projects, each showcasing our commitment to excellence and innovation.
(Provide a visually appealing UI design to display the project list, such as tiles or cards featuring images, project names, and a brief description.)

```html
<!DOCTYPE html>
<html lang="en">
<head>
<meta charset="utf-8">
<title>Zelquar Cloud — Innovative Software Solutions</title>
<link href="https://fonts.googleapis.com/css2?family=Montserrat:wght@400;500;600;700&display=swap" rel="stylesheet">
<style>
:root{
  --green:#8cc63f;
  --green-dark:#6fae22;
  --blue:#1599dc;
  --blue-dark:#0b7fc0;
  --pink:#f7c9dc;
  --pink-soft:#fdf0f5;
  --peach:#fdf1ea;
  --grey-hero:#f1f1f1;
  --ink:#333a40;
  --muted:#6b7278;
  --line:#d9dde0;
  --white:#ffffff;
}
*{box-sizing:border-box;margin:0;padding:0}
html,body{width:1200px;height:3884px;overflow:hidden}
body{font-family:"Montserrat",Arial,sans-serif;color:var(--ink);background:var(--white);position:relative}
a{color:inherit;text-decoration:none}
.abs{position:absolute}

/* header */
.site-header{position:absolute;top:0;left:0;width:1200px;height:88px;background:var(--white);display:flex;align-items:center;justify-content:space-between;padding:0 108px;box-shadow:0 2px 8px rgba(0,0,0,.06);z-index:2}
.brand{display:flex;align-items:center;gap:10px;font-weight:700;font-size:22px;color:var(--blue);letter-spacing:.5px}
.brand-dot{width:26px;height:26px;border-radius:50%;background:var(--blue)}
.main-nav{display:flex;gap:34px;font-size:15px;font-weight:500}
.main-nav a{position:relative;padding:8px 0}
.main-nav a.active{color:var(--blue);font-weight:600}
.main-nav a.active::after{content:"";position:absolute;left:-14px;right:-14px;top:-26px;height:72px;background:rgba(21,153,220,.08);z-index:-1}
.main-nav a.active::before{content:"";position:absolute;left:0;right:0;bottom:0;height:3px;background:var(--blue)}

/* hero */
.hero{position:absolute;top:88px;left:0;width:1200px;height:472px;background:linear-gradient(120deg,#f7f7f7,var(--grey-hero))}
.hero-title{position:absolute;left:108px;top:90px;font-size:46px;line-height:58px;font-weight:600;color:var(--green)}
.hero-title span{color:var(--blue)}
.hero-text{position:absolute;left:108px;top:240px;width:420px;font-size:17px;line-height:27px}
.btn{display:inline-block;background:var(--blue);color:var(--white);font-size:15px;font-weight:500;padding:10px 22px;border-radius:3px}
.hero .btn{position:absolute;left:108px;top:340px}

/* section headings */
.eyebrow{position:absolute;left:0;width:1200px;text-align:center;font-size:18px;font-weight:600;color:var(--green)}
.section-title{position:absolute;left:0;width:1200px;text-align:center;font-size:38px;font-weight:600;color:var(--blue)}
.underline{position:absolute;left:540px;width:120px;height:12px}

/* services */
.service-card{position:absolute;top:780px;width:312px;height:300px;background:var(--white);border:1px solid var(--line);border-radius:14px;box-shadow:0 6px 16px rgba(0,0,0,.08);text-align:center;padding-top:20px}
.service-art{width:110px;height:100px;margin:0 auto;border-radius:12px}
.service-card h3{font-size:22px;font-weight:500;color:var(--blue);margin:18px 0 10px}
.service-card p{font-size:13px;line-height:19px;color:var(--muted);padding:0 44px}
.badge{position:absolute;left:50%;bottom:-24px;margin-left:-24px;width:48px;height:48px;border-radius:50%;background:var(--white);box-shadow:0 3px 8px rgba(0,0,0,.15)}
.badge::after{content:"";position:absolute;inset:14px;border-radius:50%;background:var(--blue)}

/* journey */
.journey{position:absolute;top:1160px;left:0;width:1200px;height:780px;background:linear-gradient(180deg,var(--pink-soft),#fde6ef)}
.phase-one{position:absolute;left:108px;top:1392px;width:984px;height:108px;background:var(--pink);border-radius:14px 14px 0 0;padding:16px 0 0 400px;color:var(--white)}
.phase-one .phase-lead{white-space:nowrap;font-size:13.5px}
.phase-two{position:absolute;left:108px;top:1500px;width:984px;height:412px;background:var(--blue);border-radius:0 0 14px 14px;padding:24px 40px 0 400px;color:var(--white)}
.phase-num{font-size:15px;font-weight:500}
.phase-name{font-size:20px;font-weight:600;margin:4px 0 6px}
.phase-lead{font-size:14px;line-height:21px}
.steps{list-style:none;margin-top:20px}
.steps li{position:relative;padding-left:34px;margin-bottom:16px}
.steps li svg{position:absolute;left:0;top:1px}
.steps h4{font-size:15px;font-weight:600;margin-bottom:4px}
.steps p{font-size:12.5px;line-height:18px;opacity:.92}
.journey-photo{position:absolute;left:108px;top:1456px;width:372px;height:424px;background:linear-gradient(135deg,#1c2b3a,#3b5b7a 55%,#0f1a25);border-radius:0 0 0 14px}

/* industries */
.industry-card{position:absolute;top:2212px;height:176px;border:2px solid #bdbdbd;border-radius:16px;background:var(--white);display:flex;align-items:center;gap:26px;padding:0 26px}
.industry-art{width:110px;height:110px;border-radius:50%;flex:none;border:8px solid #dff0c5}
.industry-card h3{font-size:22px;font-weight:500;color:var(--blue);margin-bottom:10px}
.industry-card p{font-size:13px;line-height:19px;color:var(--muted)}
.arrow{position:absolute;top:2286px}

/* contact */
.contact{position:absolute;top:2460px;left:0;width:1200px;height:580px;background:var(--peach)}
.contact-label{position:absolute;left:108px;top:2560px;font-size:18px;font-weight:600;color:var(--green)}
.contact-title{position:absolute;left:108px;top:2596px;font-size:36px;font-weight:600;color:var(--blue)}
.field{position:absolute;height:36px;background:#f3e2e6;border:1px solid #ecd3d9;font-size:12px;color:var(--muted);padding:10px 12px}
.submit{position:absolute;left:108px;top:2916px;padding:8px 22px}
.reach-label{position:absolute;left:708px;top:2642px;font-size:18px;font-weight:600;color:var(--blue)}
.reach-phone{position:absolute;left:708px;top:2676px;font-size:38px;font-weight:500;color:var(--green)}
.reach-text{position:absolute;left:708px;top:2740px;width:330px;font-size:13px;line-height:19px;color:var(--muted)}
.map-link{position:absolute;left:708px;top:2814px;display:flex;align-items:center;gap:14px;font-size:15px;color:var(--blue);text-decoration:underline}
.map-pin{width:40px;height:40px;border-radius:50%;background:var(--blue);display:flex;align-items:center;justify-content:center}

/* about */
.about-photo{position:absolute;left:140px;top:3140px;width:440px;height:320px;background:linear-gradient(135deg,#4b6478,#9fb3c2 55%,#2c3d4c)}
.about-bar{position:absolute;left:120px;top:3460px;width:200px;height:22px;background:var(--blue)}
.play{position:absolute;left:328px;top:3268px;width:64px;height:64px;border-radius:50%;background:var(--green);display:flex;align-items:center;justify-content:center}
.about-label{position:absolute;left:624px;top:3124px;font-size:18px;font-weight:600;color:var(--green)}
.about-title{position:absolute;left:624px;top:3160px;font-size:36px;line-height:44px;font-weight:600;color:var(--blue)}
.about-text{position:absolute;left:624px;width:470px;font-size:14px;line-height:20px;color:var(--muted)}
.about-btn{position:absolute;left:624px;top:3482px;padding:7px 18px;font-size:14px}

/* footer */
.site-footer{position:absolute;top:3572px;left:0;width:1200px;height:268px;background:var(--green);color:var(--white)}
.footer-brand{position:absolute;left:108px;top:40px;display:flex;align-items:center;gap:10px;font-size:22px;font-weight:700}
.footer-brand .brand-dot{background:var(--white)}
.footer-blurb{position:absolute;left:108px;top:100px;width:230px;font-size:13px;line-height:19px}
.socials{position:absolute;left:108px;top:160px;display:flex;gap:10px}
.socials span{width:26px;height:26px;border-radius:50%;border:2px solid var(--white)}
.footer-col{position:absolute;top:40px}
.footer-col h4{font-size:18px;font-weight:600;margin-bottom:14px}
.footer-col li{list-style:none;font-size:13px;margin-bottom:7px;display:flex;align-items:center;gap:8px}
.footer-col li::before{content:"";width:6px;height:6px;border-radius:50%;background:var(--white);flex:none}
.footer-col.info li::before{display:none}
.copyright{position:absolute;top:3840px;left:0;width:1200px;height:44px;background:var(--blue);color:var(--white);font-size:13px;display:flex;align-items:center;justify-content:center}
</style>
</head>
<body>

<header class="site-header">
  <a class="brand" href="#"><span class="brand-dot"></span>ZELQUAR CLOUD</a>
  <nav class="main-nav">
    <a class="active" href="#">Home</a>
    <a href="#">About Us</a>
    <a href="#">Software Development</a>
    <a href="#">Industries</a>
    <a href="#">Contact Us</a>
  </nav>
</header>

<section class="hero">
  <h1 class="hero-title">Innovative Solutions for<br>Your <span>Business Needs</span></h1>
  <p class="hero-text">Where we specialize in providing high-quality software solutions designed to help businesses thrive.</p>
  <a class="btn" href="#">Get Started</a>
</section>

<section class="services">
  <p class="eyebrow" style="top:650px">Our Services</p>
  <h2 class="section-title" style="top:680px">Innovative Solutions, Seamless Integration</h2>
  <svg class="underline" style="top:734px" viewBox="0 0 120 12"><path d="M5 8 Q60 0 115 8" fill="none" stroke="var(--green)" stroke-width="2.5"/></svg>

  <article class="service-card" style="left:108px">
    <div class="service-art" role="img" aria-label="Illustration of product development" style="background:linear-gradient(135deg,#f7a23b,#e8355a)"></div>
    <h3>Product Development</h3>
    <p>From concept to completion, we help you bring innovative products to life.</p>
    <span class="badge"></span>
  </article>
  <article class="service-card" style="left:444px">
    <div class="service-art" role="img" aria-label="Illustration of app development" style="background:linear-gradient(135deg,#6ec1f0,#e85aa0)"></div>
    <h3>App Development</h3>
    <p>Build cutting-edge mobile and desktop applications to engage your audience and enhance operational efficiency.</p>
    <span class="badge"></span>
  </article>
  <article class="service-card" style="left:780px">
    <div class="service-art" role="img" aria-label="Illustration of website development" style="background:linear-gradient(135deg,#4aa6e6,#f28a3a)"></div>
    <h3>Website Development</h3>
    <p>Your website is the face of your business. We ensure it leaves a lasting impression.</p>
    <span class="badge"></span>
  </article>
</section>

<section class="journey"></section>
<p class="eyebrow" style="top:1246px">Your Journey with Us</p>
<h2 class="section-title" style="top:1278px">Transforming Your Vision into Reality</h2>
<svg class="underline" style="top:1332px" viewBox="0 0 120 12"><path d="M5 8 Q60 0 115 8" fill="none" stroke="var(--green)" stroke-width="2.5"/></svg>

<div class="phase-one">
  <p class="phase-num">&lt; 01 &gt;</p>
  <p class="phase-name">Phase One: Discovery</p>
  <p class="phase-lead">We start by understanding your business inside and out, ensuring alignment.</p>
</div>
<div class="phase-two">
  <p class="phase-num">&lt; 02 &gt;</p>
  <p class="phase-name">Phase Two: Estimate</p>
  <p class="phase-lead">We present a fully customized solution tailored to your needs, empowering you with the information required to make confident decisions.</p>
  <ul class="steps">
    <li><svg width="20" height="20" viewBox="0 0 20 20"><circle cx="10" cy="10" r="9" fill="#fff"/><path d="M5.5 10.5l3 3 6-6" fill="none" stroke="var(--blue)" stroke-width="2"/></svg>
      <h4>Technology Plan &amp; Roadmap</h4><p>We design a detailed technology roadmap that includes the functionalities you need, the ideal tools and technologies, and a timeline for project completion.</p></li>
    <li><svg width="20" height="20" viewBox="0 0 20 20"><circle cx="10" cy="10" r="9" fill="#fff"/><path d="M5.5 10.5l3 3 6-6" fill="none" stroke="var(--blue)" stroke-width="2"/></svg>
      <h4>Transition Planning</h4><p>Our scope includes planning for a seamless transition, covering everything from system migration to user training and long-term usability.</p></li>
    <li><svg width="20" height="20" viewBox="0 0 20 20"><circle cx="10" cy="10" r="9" fill="#fff"/><path d="M5.5 10.5l3 3 6-6" fill="none" stroke="var(--blue)" stroke-width="2"/></svg>
      <h4>Future Forecasting</h4><p>Our solutions are built to grow with your business. We consider scalability, future technology trends, and your organization’s long-term needs to ensure lasting success.</p></li>
  </ul>
</div>
<div class="journey-photo" role="img" aria-label="Photo of hands typing on a laptop showing code"></div>

<section class="industries">
  <p class="eyebrow" style="top:2066px">Industries We Serve</p>
  <h2 class="section-title" style="top:2098px">Serving Diverse Industries with Expertise</h2>
  <svg class="underline" style="top:2152px" viewBox="0 0 120 12"><path d="M5 8 Q60 0 115 8" fill="none" stroke="var(--green)" stroke-width="2.5"/></svg>

  <svg class="arrow" style="left:64px" width="20" height="28" viewBox="0 0 20 28"><path d="M15 3L5 14l10 11" fill="none" stroke="#111" stroke-width="4"/></svg>
  <article class="industry-card" style="left:148px;width:432px">
    <div class="industry-art" role="img" aria-label="Illustration of payroll calculations" style="background:linear-gradient(135deg,#f3c64a,#8cc63f)"></div>
    <div><h3>Payroll Sector</h3><p>Sed ut perspiciatis unde omnis iste natus error sit voluptatem accusantium doloremque laudantium.</p></div>
  </article>
  <article class="industry-card" style="left:612px;width:476px">
    <div class="industry-art" role="img" aria-label="Illustration of education and learning" style="background:linear-gradient(135deg,#e8355a,#1599dc)"></div>
    <div><h3>Education</h3><p>Sed ut perspiciatis unde omnis iste natus error sit voluptatem accusantium doloremque laudantium.</p></div>
  </article>
  <svg class="arrow" style="left:1112px" width="20" height="28" viewBox="0 0 20 28"><path d="M5 3l10 11L5 25" fill="none" stroke="#111" stroke-width="4"/></svg>
</section>

<section class="contact" role="img" aria-label="Faint world map background"></section>
<p class="contact-label">Contact Us</p>
<h2 class="contact-title">Reach Out for Solutions</h2>
<svg class="abs" style="left:108px;top:2648px" width="120" height="12" viewBox="0 0 120 12"><path d="M5 8 Q60 0 115 8" fill="none" stroke="var(--green)" stroke-width="2.5"/></svg>
<div class="field" style="left:108px;top:2690px;width:262px">Name</div>
<div class="field" style="left:380px;top:2690px;width:260px">Phone Number</div>
<div class="field" style="left:108px;top:2746px;width:532px">Email Address</div>
<div class="field" style="left:108px;top:2802px;width:532px;height:96px">Please describe what you need</div>
<a class="btn submit" href="#">Submit</a>

<p class="reach-label">Reach out now!</p>
<p class="reach-phone">+1 555 0142 7788</p>
<p class="reach-text">Start the collaboration with us while figuring out the best solution based on your needs.</p>
<a class="map-link" href="#"><span class="map-pin"><svg width="16" height="22" viewBox="0 0 16 22"><path d="M8 1a7 7 0 0 0-7 7c0 5 7 13 7 13s7-8 7-13a7 7 0 0 0-7-7z" fill="#fff"/><circle cx="8" cy="8" r="2.6" fill="var(--blue)"/></svg></span>View on Map</a>

<section class="about">
  <div class="about-photo" role="img" aria-label="Photo of a developer working at multiple screens"></div>
  <div class="about-bar"></div>
  <div class="play"><svg width="22" height="24" viewBox="0 0 22 24"><path d="M3 2l17 10L3 22z" fill="#fff"/></svg></div>
  <p class="about-label">About Zelquar Cloud</p>
  <h2 class="about-title">Driven by Innovation &amp;<br>Excellence</h2>
  <svg class="abs" style="left:624px;top:3252px" width="120" height="12" viewBox="0 0 120 12"><path d="M5 8 Q60 0 115 8" fill="none" stroke="var(--green)" stroke-width="2.5"/></svg>
  <p class="about-text" style="top:3276px">Lorem ipsum dolor sit amet, consectetur adipiscing elit, sed do eiusmod tempor incididunt ut labore et dolore magna aliqua. Quis ipsum suspendisse ultrices gravida. Risus commodo viverra maecenas accumsan lacus vel facilisis.</p>
  <p class="about-text" style="top:3382px">Lorem ipsum dolor sit amet, consectetur adipiscing elit, sed do eiusmod tempor incididunt ut labore et dolore magna aliqua. Quis ipsum suspendisse.</p>
  <a class="btn about-btn" href="#">Read More</a>
</section>

<footer class="site-footer">
  <div class="footer-brand"><span class="brand-dot"></span>ZELQUAR CLOUD</div>
  <p class="footer-blurb">Empower your business with tailored software solutions built for growth.</p>
  <div class="socials"><span></span><span></span><span></span><span></span><span></span></div>

  <div class="footer-col" style="left:410px">
    <h4>Quick Links</h4>
    <ul><li>Home</li><li>About Us</li><li>Software Development</li><li>Industries</li><li>Contact Us</li></ul>
  </div>
  <div class="footer-col" style="left:668px">
    <h4>Other Links</h4>
    <ul><li>FAQs</li><li>Help Center</li><li>Terms &amp; Conditions</li><li>Privacy Policy</li><li>Sitemap</li></ul>
  </div>
  <div class="footer-col info" style="left:890px">
    <h4>Contact Info</h4>
    <ul>
      <li><svg width="14" height="18" viewBox="0 0 16 22"><path d="M8 1a7 7 0 0 0-7 7c0 5 7 13 7 13s7-8 7-13a7 7 0 0 0-7-7z" fill="#fff"/></svg>120 Harbor Lane, Suite 4</li>
      <li><svg width="14" height="14" viewBox="0 0 16 16"><path d="M3 1l3 1 1 4-2 1a9 9 0 0 0 4 4l1-2 4 1 1 3-2 2C7 15 1 9 1 3z" fill="#fff"/></svg>+1 555 0142 7788</li>
      <li><svg width="14" height="12" viewBox="0 0 16 12"><rect x="1" y="1" width="14" height="10" fill="none" stroke="#fff" stroke-width="1.6"/><path d="M1 1l7 6 7-6" fill="none" stroke="#fff" stroke-width="1.6"/></svg>hello@zelquarcloud.com</li>
    </ul>
  </div>
</footer>
<div class="copyright">© 2024 Zelquar Cloud. All rights reserved.</div>

</body>
</html>
```